Flyer-Design für ein Baumhaushotel
Zielgruppe
Baumhaushotel. Hochwertige und gehobene Ausstattung. Fokus Natur und Ruhe.
Naturliebhaber, Großstadtmensch der eine Auszeit sucht
Aufgabenstellung
Flyer dreichfach gefaltet, beidseitig bedruckt
Fotos haben wir hochgeladen, eine höhere Auflösung ist auch vorhanden.
Texte können auch gern von unserer Website genommen werden: waldnest-kojen.de
Nicht zu viel Text, z.B. diesen Text:
evtl einfach nur Stichwörter locker einfügen wie zB (dies ist nur eine Auswahl)
zwischen den Bäumen träumen
in vier Metern Höhe
barrierefreies Baumhaus mit vielen Features
Kaminofen
Bad mit Dusche & WC
Pantry-Küche
gemütlich
Echtholzfußboden
atemberaubende Ausblicke, hoher Komfort und Natur pur.
an einem Seengebiet in der Nähe des Deiches, hinter dem die Elbe in die Nordsee mündet.
eine besondere Auszeit hoch über dem Erdboden
Wenn vom Design sinnvoll, kann man noch Vorteile einbringen wie zB etwas von dieser Auflistung (muss aber auch nicht genannt werden)
! auf jeden Fall soll unser barrierefreies Kiebitz-Baumhaus genannt und gezeigt werden !
30qm Baumhäuser in vier Meter Höhe inkl. Bad und Pantry-Küche, Schlafbereich, Couchecke und Essbereich
10qm Außenterrasse auf 2,50m Höhe inkl. Strandkorb
einzigartiges großes barrierefreies Baumhaus (57qm) , mit barrierefreiem Bad und vielen Features sowie Fußbodenerwärmung, dieses Haus ist für bis zu 6 Personen nutzbar, alle anderen Baumhäuser bis zu 4 Personen
Wlan, TV, Heizung, Kaminofen und voll ausgestattete Küche
Parkplatz direkt im Einfahrtbereich inklusive – das Baumhaushotel-Gelände selbst ist autofrei
haustierfreie und haustierfreundliche Baumhäuser verfügbar
Bettwäsche, Handtücher und Kaminholz inklusive
hoteleigene Kanus und Bootsanleger am Drei-Seengebiet inklusive
von alten Bäumen umgebendes Baumhausgelände inkl. Waldbad (im Sinne von Shinrin Yoku)
Baumhaushotel liegt direkt neben Drei-Seengebiet und in Deichnähe zur Elbe/ Nordsee
spezieller Rückzugsbereich für Tiere, den wir Menschen nicht betreten – Tierbeo..

```html
<!DOCTYPE html>
<html lang="de">
<head>
<meta charset="utf-8">
<title>Waldnest-Kojen – Flyer</title>
<link rel="stylesheet" href="https://fonts.googleapis.com/css2?family=Bebas+Neue&family=Montserrat:wght@400;500;600&display=swap">
<style>
  :root {
    --forest: #37504d;
    --sage: #c6dcc0;
    --sage-text: #c9dfc3;
    --paper: #ffffff;
    --stage: #dedede;
    --headline: "Bebas Neue", "Oswald", sans-serif;
    --body: "Montserrat", sans-serif;
  }
  * { box-sizing: border-box; margin: 0; padding: 0; }
  html, body { width: 1160px; height: 1200px; overflow: hidden; background: var(--stage); }
  .spread {
    position: absolute; left: 210px; width: 740px; height: 574px;
    background: var(--sage); font-family: var(--body); overflow: hidden;
  }
  .spread--outer { top: 18px; }
  .spread--inner { top: 608px; }
  .spread > svg { position: absolute; inset: 0; width: 740px; height: 574px; }
  .block { position: absolute; }
  .headline { font-family: var(--headline); font-weight: 400; letter-spacing: 0.5px; line-height: 1.12; }
  .headline--pale { color: var(--sage-text); }
  .headline--dark { color: var(--forest); }
  .site-name { font-family: var(--body); font-weight: 600; color: var(--sage-text); font-size: 13px; line-height: 1; letter-spacing: 0.2px; }
  .site-name--on-sage { color: var(--paper); }
  .copy { font-size: 9px; line-height: 1.6; }
  .copy--pale { color: var(--sage-text); }
  .copy--dark { color: var(--forest); }
  .address { font-size: 6.8px; line-height: 1.95; color: var(--forest); text-align: center; font-style: normal; }
  .amenities { list-style: none; text-align: center; color: var(--sage-text); font-size: 7px; line-height: 1.65; }
  .amenities li { margin-bottom: 9px; }
  .features { list-style: none; color: var(--paper); font-size: 9.2px; font-weight: 500; line-height: 1.85; }
  .features li::before { content: ""; display: inline-block; width: 4px; height: 4px; background: var(--paper); margin: 0 6px 1px 0; vertical-align: middle; }
  .highlights { list-style: none; color: var(--forest); font-size: 8.8px; line-height: 1.75; }
  .highlights li { position: relative; padding-left: 10px; margin-bottom: 12px; }
  .highlights li::before { content: ""; position: absolute; left: 0; top: 5px; width: 4px; height: 4px; background: var(--forest); }
  .badge-text { font-family: var(--headline); font-size: 19px; fill: var(--forest); }
</style>
</head>
<body>

<!-- Außenseite -->
<section class="spread spread--outer" aria-label="Flyer Außenseite">
  <svg viewBox="0 0 740 574">
    <defs>
      <linearGradient id="tone-facade" x1="0" y1="0" x2="1" y2="1"><stop offset="0" stop-color="#8a6a45"/><stop offset="0.6" stop-color="#c9a677"/><stop offset="1" stop-color="#e4ddd2"/></linearGradient>
      <linearGradient id="tone-room" x1="0" y1="0" x2="1" y2="1"><stop offset="0" stop-color="#c4a27a"/><stop offset="0.5" stop-color="#e6ddd0"/><stop offset="1" stop-color="#6f5238"/></linearGradient>
      <linearGradient id="tone-dusk" x1="0" y1="0" x2="0" y2="1"><stop offset="0" stop-color="#5d6a86"/><stop offset="0.6" stop-color="#2a3a32"/><stop offset="1" stop-color="#3f6b34"/></linearGradient>
      <linearGradient id="tone-stilts" x1="0" y1="0" x2="0" y2="1"><stop offset="0" stop-color="#b9c2b3"/><stop offset="0.35" stop-color="#b79a6c"/><stop offset="0.7" stop-color="#5f7a3a"/><stop offset="1" stop-color="#8c7a5c"/></linearGradient>
    </defs>
    <polygon points="0,0 246,0 246,158 0,252" fill="var(--forest)"/>
    <polygon points="0,252 246,158 246,318 0,305" fill="url(#tone-facade)" stroke="#fff" stroke-width="2" role="img" aria-label="Foto: Holzfassade des Kiebitz-Baumhauses mit Namensschild"/>
    <polygon points="0,305 246,318 246,516 0,428" fill="url(#tone-room)" stroke="#fff" stroke-width="2" role="img" aria-label="Foto: Wohn- und Schlafbereich im Kiebitz-Baumhaus"/>
    <polygon points="246,0 493,0 493,196 246,162" fill="var(--sage)"/>
    <polygon points="246,162 493,196 493,574 246,574" fill="var(--forest)" stroke="#fff" stroke-width="2"/>
    <polygon points="493,0 740,0 740,209 493,256" fill="var(--forest)"/>
    <polygon points="493,256 740,209 740,362 493,330" fill="url(#tone-dusk)" stroke="#fff" stroke-width="2" role="img" aria-label="Foto: beleuchtete Baumhäuser zwischen Bäumen in der Dämmerung"/>
    <polygon points="493,330 740,362 740,574 493,574" fill="url(#tone-stilts)" stroke="#fff" stroke-width="2" role="img" aria-label="Foto: Baumhäuser auf Stelzen im Grünen"/>
    <g transform="translate(678,358)">
      <circle r="41" fill="var(--sage)" stroke="var(--forest)" stroke-width="2.5"/>
      <text class="badge-text" text-anchor="middle" transform="rotate(-10)"><tspan x="0" y="-3">JETZT</tspan><tspan x="0" y="17">BUCHEN!</tspan></text>
    </g>
  </svg>

  <h2 class="block headline headline--pale" style="left:30px;top:28px;font-size:31px;">BARRIEREFREIES<br>KIEBITZ-BAUMHAUS</h2>
  <p class="block copy copy--pale" style="left:30px;top:114px;width:200px;">Einzigartiges großes barrierefreies Baumhaus (57qm), mit barrierefreiem Bad und vielen Features sowie Fußbodenerwärmung.</p>
  <p class="block copy copy--dark" style="left:30px;top:492px;width:150px;">Dieses Haus ist für bis zu 6 Personen nutzbar, alle anderen Baum&shy;häuser bis zu 4 Personen.</p>

  <p class="block site-name site-name--on-sage" style="left:246px;width:247px;top:42px;text-align:center;">waldnest-kojen.de</p>
  <address class="block address" style="left:246px;width:247px;top:78px;">
    Baumhaushotel an der Elbe/Nordsee<br>Birkenhainer Weg 7<br>21999 Moorlinden<br>+49 (0) 1500 000 0000<br>E-Mail: post@waldnest-kojen.de
  </address>
  <h2 class="block headline headline--pale" style="left:246px;width:247px;top:204px;font-size:31px;text-align:center;">SONSTIGE<br>AUSSTATTUNG</h2>
  <ul class="block amenities" style="left:276px;width:187px;top:286px;">
    <li>Wlan, TV, Heizung, Kaminofen und voll ausgestattete Küche</li>
    <li>Parkplatz direkt im Einfahrtbereich inklusive – das Baumhaushotel-Gelände selbst ist autofrei</li>
    <li>Haustierfreie und haustierfreundliche Baumhäuser verfügbar</li>
    <li>Bettwäsche, Handtücher und Kaminholz inklusive</li>
    <li>Hoteleigene Kanus und Bootsanleger am Drei-Seengebiet inklusive</li>
    <li>Von alten Bäumen umgebendes Baumhausgelände inkl. Waldbad (im Sinne von Shinrin Yoku)</li>
    <li>Baumhaushotel liegt direkt neben Drei-Seengebiet und in Deichnähe zur Elbe/ Nordsee</li>
    <li>Spezieller Rückzugsbereich für Tiere, den wir Menschen nicht betreten – Tierbeobachtungen möglich</li>
  </ul>

  <p class="block site-name" style="left:493px;width:247px;top:42px;text-align:center;">waldnest-kojen.de</p>
  <h1 class="block headline headline--pale" style="left:520px;top:82px;font-size:41px;line-height:1.08;">ZWISCHEN<br>DEN BÄUMEN<br>TRÄUMEN</h1>
</section>

<!-- Innenseite -->
<section class="spread spread--inner" aria-label="Flyer Innenseite">
  <svg viewBox="0 0 740 574">
    <defs>
      <linearGradient id="tone-loft" x1="0" y1="0" x2="1" y2="1"><stop offset="0" stop-color="#b07c4c"/><stop offset="0.5" stop-color="#d9cfc0"/><stop offset="1" stop-color="#7d5a3c"/></linearGradient>
      <linearGradient id="tone-terrace" x1="0" y1="0" x2="1" y2="1"><stop offset="0" stop-color="#3f4452"/><stop offset="0.6" stop-color="#6f8a4a"/><stop offset="1" stop-color="#b08457"/></linearGradient>
      <linearGradient id="tone-reading" x1="0" y1="0" x2="1" y2="0"><stop offset="0" stop-color="#2e2a22"/><stop offset="0.45" stop-color="#6e8a3c"/><stop offset="1" stop-color="#4a4238"/></linearGradient>
      <linearGradient id="tone-kitchen" x1="0" y1="0" x2="1" y2="1"><stop offset="0" stop-color="#c9c3b6"/><stop offset="0.5" stop-color="#9c6c44"/><stop offset="1" stop-color="#2f3b44"/></linearGradient>
      <linearGradient id="tone-stove" x1="0" y1="0" x2="1" y2="0"><stop offset="0" stop-color="#9a6a3e"/><stop offset="0.55" stop-color="#3a3634"/><stop offset="1" stop-color="#d9d3ca"/></linearGradient>
    </defs>
    <polygon points="194,0 496,0 496,212 248,238" fill="url(#tone-loft)" stroke="#fff" stroke-width="2" role="img" aria-label="Foto: Innenraum mit Küche, Leiter zur Empore und Schlafnische"/>
    <polygon points="0,190 248,238 288,375 0,456" fill="url(#tone-terrace)" stroke="#fff" stroke-width="2" role="img" aria-label="Foto: Terrasse mit Strandkorb, Tisch und Stühlen"/>
    <polygon points="0,456 288,375 349,574 0,574" fill="url(#tone-reading)" stroke="#fff" stroke-width="2" role="img" aria-label="Foto: lesende Person am Fenster mit Blick auf Wiese und Containerschiff"/>
    <polygon points="496,0 740,0 740,159 496,212" fill="var(--forest)"/>
    <polygon points="496,212 740,159 740,329 468,389" fill="url(#tone-kitchen)" stroke="#fff" stroke-width="2" role="img" aria-label="Foto: Küche und Essbereich mit Holzboden"/>
    <polygon points="468,389 740,329 740,574 446,574" fill="url(#tone-stove)" stroke="#fff" stroke-width="2" role="img" aria-label="Foto: Kaminofen mit brennendem Feuer"/>
    <g transform="translate(318,488)">
      <circle r="41" fill="var(--sage)" stroke="var(--forest)" stroke-width="2.5"/>
      <text class="badge-text" text-anchor="middle" transform="rotate(-10)"><tspan x="0" y="-3">JETZT</tspan><tspan x="0" y="17">BUCHEN!</tspan></text>
    </g>
  </svg>

  <h2 class="block headline headline--dark" style="left:30px;top:30px;font-size:29px;line-height:1.14;">ATEMBERAUBENDE<br>AUSBLICKE, HOHER<br>KOMFORT UND<br>NATUR PUR.</h2>

  <ul class="block highlights" style="left:283px;top:260px;width:180px;">
    <li>atemberaubende Ausblicke, hoher Komfort und Natur pur.</li>
    <li style="margin-left:10px;">an einem Seengebiet in der Nähe des Deiches, hinter dem die Elbe in die Nordsee mündet.</li>
    <li style="margin-left:26px;">eine besondere Auszeit hoch über dem Erdboden</li>
  </ul>

  <p class="block site-name" style="left:522px;top:36px;">waldnest-kojen.de</p>
  <ul class="block features" style="left:522px;top:66px;">
    <li>in vier Metern Höhe</li>
    <li>eigener Strandkorb</li>
    <li>Kaminofen</li>
    <li>Bad mit Dusche &amp; WC</li>
    <li>Pantry-Küche</li>
    <li>gemütlicher Echtholzfußboden</li>
  </ul>
</section>

</body>
</html>
```